Vorlix Word Documentation Template

Create word documentation template for Vorlix. This should include cover page, table of contect, list of tables, different style heading etc. The template needs to be inline with vorlix.com.au website in terms of colors and style, needs to be clean and simple. We are providing professional services in technology sector. The final design should communicate clean, professional and modern approach
Updates

Project has been changed to non-refundable and Vector Logo uploaded

Project Deadline Extended
Reason: Have changed project to non-refundable and uploaded vector logo. Extending deadline by another 10 days.

Project Deadline Extended

Industry/Entity Type

It Professional

```html
<!DOCTYPE html>
<html lang="en">
<head>
<meta charset="utf-8">
<title>Vorlix Business Proposal – Terms &amp; Conditions</title>
<link rel="stylesheet" href="https://fonts.googleapis.com/css2?family=Open+Sans:wght@400;600;700;800&display=swap">
<style>
  :root {
    --backdrop: #ececec;
    --paper: #f1f1f1;
    --panel: #c9c9c9;
    --band: #e2e2e2;
    --orange: #e8692c;
    --title-grey: #9a9a9a;
    --ink: #2b2b2b;
    --body-ink: #3a3a3a;
    --dark: #333333;
    --label-grey: #7a7a7a;
  }
  * { box-sizing: border-box; margin: 0; padding: 0; }
  html, body {
    width: 1200px; height: 795px; overflow: hidden;
    background: var(--backdrop);
    font-family: "Open Sans", Arial, sans-serif;
  }
  .page {
    position: absolute; left: 333px; top: 20px;
    width: 534px; height: 755px;
    background: var(--paper);
    overflow: hidden;
    box-shadow: 0 2px 10px rgba(0,0,0,0.12);
  }
  .corner-accent { position: absolute; }
  .corner-accent--top { right: 0; top: 0; width: 180px; height: 130px; }
  .corner-accent--bottom { right: 0; bottom: 0; width: 150px; height: 110px; }

  .title-band {
    position: absolute; left: 0; top: 54px; width: 310px; height: 44px;
    background: var(--band);
  }
  .running-head {
    position: absolute; left: 0; top: 22px; height: 26px;
    display: flex; align-items: center;
  }
  .page-number {
    width: 44px; height: 26px; background: var(--orange); color: #fff;
    font-size: 13px; font-weight: 400;
    display: flex; align-items: center; justify-content: center;
  }
  .running-head__label {
    margin-left: 12px; padding-left: 12px; border-left: 1px solid #b5b5b5;
    font-size: 8px; letter-spacing: 0.6px; color: var(--label-grey);
    line-height: 14px;
  }
  .page-title {
    position: absolute; left: 54px; top: 58px;
    font-size: 36px; font-weight: 800; letter-spacing: 0.5px;
    color: var(--title-grey); line-height: 40px;
  }
  .page-title__accent { color: var(--orange); }

  .content-panel {
    position: absolute; left: 54px; top: 112px; width: 420px; height: 470px;
    background: var(--panel);
    padding: 14px 16px;
  }
  .section-heading {
    font-size: 11px; font-weight: 700; color: var(--ink);
    margin-bottom: 8px;
  }
  .section + .section { margin-top: 34px; }
  .section p {
    font-size: 7.4px; line-height: 11px; color: var(--body-ink);
    margin-bottom: 11px;
  }

  .dot-cluster {
    position: absolute; left: 482px; top: 300px; width: 44px; height: 120px;
    border-radius: 22px;
    background: linear-gradient(180deg, #e8692c 0%, #9c5638 45%, #333333 70%, #e8692c 100%);
    opacity: 0.85;
  }
</style>
</head>
<body>
  <article class="page">
    <svg class="corner-accent corner-accent--top" viewBox="0 0 180 130" aria-hidden="true">
      <polyline points="0,3 177,3 177,130" fill="none" stroke="var(--orange)" stroke-width="6"/>
    </svg>

    <div class="title-band"></div>

    <header class="running-head">
      <div class="page-number">16</div>
      <div class="running-head__label">BUSINESS PROPOSAL</div>
    </header>

    <h1 class="page-title">TERMS &amp; <span class="page-title__accent">CONDITIONS</span></h1>

    <main class="content-panel">
      <section class="section">
        <h2 class="section-heading">Mauris quam dolor, cursus at porta et, luctus eget purus.</h2>
        <p>Nunc tempor luctus interdum. Duis libero leo, consequat ut accumsan eu, viverra et erat. Donec nec lorem et tellus mollis lobortis. Integer sed dolor ut leo porta mollis. Proin eu augue augue. Duis id velit in arcu accumsan congue. Donec at massa id risus varius eleifend vitae at quam. Vivamus tristique est vitae felis vehicula mollis. Vivamus quam dolor, tempor ac gravida sit amet, porta fermentum magna. Aliquam euismod commodo nisl, vel luctus lorem fermentum quis.</p>
        <p>Duis quis purus adipiscing mi scelerisque dictum quis vel eros. Nullam eu tempor purus. Mauris quam dolor, cursus at porta et, luctus eget purus. Nunc tempor luctus interdum. Integer sed dolor ut leo porta mollis. Donec at massa id risus varius eleifend vitae at quam.</p>
        <p>Vivamus tristique est vitae felis vehicula mollis. Vivamus quam dolor, tempor ac gravida sit amet, porta fermentum magna. Aliquam euismod commodo nisl, vel luctus lorem fermentum quis.</p>
      </section>
      <section class="section">
        <h2 class="section-heading">Mauris quam dolor, cursus at porta et.</h2>
        <p>Nunc tempor luctus interdum. Duis libero leo, consequat ut accumsan eu, viverra et erat. Donec nec lorem et tellus mollis lobortis. Integer sed dolor ut leo porta mollis. Proin eu augue augue. Duis id velit in arcu accumsan congue. Donec at massa id risus varius eleifend vitae at quam. Vivamus tristique est vitae felis vehicula mollis. Vivamus quam dolor, tempor ac gravida sit amet, porta fermentum magna. Aliquam euismod commodo nisl, vel luctus lorem fermentum quis.</p>
        <p>Duis quis purus adipiscing mi scelerisque dictum quis vel eros. Nullam eu tempor purus. Mauris quam dolor, cursus at porta et, luctus eget purus. Nunc tempor luctus interdum. Integer sed dolor ut leo porta mollis. Donec at massa id risus varius eleifend vitae at quam.</p>
        <p>Vivamus tristique est vitae felis vehicula mollis. Vivamus quam dolor, tempor ac gravida sit amet, porta fermentum magna. Aliquam euismod commodo nisl, vel luctus lorem fermentum quis.</p>
      </section>
    </main>

    <div class="dot-cluster" role="img" aria-label="Decorative cluster of orange and charcoal dots"></div>

    <svg class="corner-accent corner-accent--bottom" viewBox="0 0 150 110" aria-hidden="true">
      <polyline points="0,104 144,104 144,0" fill="none" stroke="var(--dark)" stroke-width="12"/>
    </svg>
  </article>
</body>
</html>
```